Upbeat Accouting Package Flyer

I am looking for a 1 page (front, or front and back) flyer that will become our marketing for our accounting services. We are looking for something a little different and we are catering to the small retail shop owners. We have 3 accounting packages we would like to display and then some add-ons. I have included our logo that must be included in the design. I have uploaded the accounting package information as well.
Target Market(s)
Small Retail Shop Owners
Industry/Entity Type
Accounting
Colors
Designer to choose colors to be used in the design.
Requirements
Must have
- A casual feel. We are not your typical accountants who are very professional and "stuffy". I want it to feel like we are all family.
Nice to have
- I would like to incorporate some sort of retail theme.
- We have a couple of taglines we like to use and it would be great if they could be included. They are "We know you CAN do the accounting, but do you WANT to?" and "We allow you to get back to what's important."
Should not have
- Typical stock accounting photos of people shaking hands, large office buildings, etc.

```html
<!DOCTYPE html>
<html lang="en">
<head>
<meta charset="utf-8">
<title>Brightway Accounting Packages Flyer</title>
<link href="https://fonts.googleapis.com/css2?family=Montserrat:wght@600;700&family=Roboto+Condensed:ital,wght@0,400;0,700;1,700&family=Roboto:wght@500&display=swap" rel="stylesheet">
<style>
  :root{
    --stage:#333232;
    --paper:#ffffff;
    --panel-grey:#d8d9db;
    --cyan:#1fb8d6;
    --cyan-light:#a8dde9;
    --ink:#111111;
    --navy:#153a55;
    --black:#0b0b0b;
    --grey-row:#8d8e92;
    --muted:#555555;
  }
  *{margin:0;padding:0;box-sizing:border-box}
  html,body{width:946px;height:1200px;overflow:hidden;background:var(--stage)}
  .flyer{position:absolute;left:49px;top:0;width:848px;height:1200px;background:var(--paper);overflow:hidden;font-family:"Roboto Condensed",Arial,sans-serif;color:var(--ink)}
  .intro-panel{position:absolute;left:0;top:0;width:369px;height:472px;background:var(--panel-grey)}
  .shop-photo{position:absolute;left:369px;top:0;width:479px;height:472px;background:linear-gradient(160deg,#5b4a3a 0%,#a88a66 40%,#7c6a5a 70%,#3d3a3a 100%)}
  .accent-band{position:absolute;left:0;top:472px;width:848px;height:34px;background:var(--cyan)}
  .footer-band{position:absolute;left:0;bottom:0;width:848px;height:16px;background:var(--cyan)}

  .brand{position:absolute;left:35px;top:30px;color:var(--ink);font-family:"Montserrat",sans-serif;font-weight:700}
  .brand-name{font-size:50px;line-height:1;letter-spacing:-0.5px}
  .brand-sub{font-size:11px;text-align:right;letter-spacing:0.3px;margin-top:-2px}

  .tagline{position:absolute;left:38px;top:128px;font-size:30px;line-height:31px;color:var(--ink)}
  .tagline em{font-style:italic;font-weight:700;color:var(--cyan)}
  .title{position:absolute;left:35px;top:246px;font-family:"Roboto",sans-serif;font-weight:500;line-height:1;letter-spacing:-1px}
  .title .line1{font-size:40px}
  .title .line2{font-size:53px;margin-top:2px}
  .price{position:absolute;left:35px;top:355px;font-size:14px;font-weight:700}
  .price b{font-size:20px}

  .package{position:absolute;display:flex;flex-direction:column}
  .package.develop{left:56px;top:415px;width:221px;height:520px;background:var(--cyan)}
  .package.relax{left:568px;top:415px;width:223px;height:520px;background:var(--cyan)}
  .package.grow{left:298px;top:355px;width:254px;height:623px;background:var(--black);box-shadow:0 4px 10px rgba(0,0,0,.35)}
  .pill{margin:8px 11px 0;height:38px;border-radius:10px;background:var(--black);color:#fff;font-weight:700;font-size:28px;display:flex;align-items:center;justify-content:center}
  .grow .pill{background:#fff;color:var(--ink);height:40px;margin-top:10px}
  .icon-slot{height:83px;display:flex;align-items:center;justify-content:center;flex-direction:column}
  .grow .icon-slot{height:89px}
  .icon-placeholder{width:60px;height:60px;border-radius:50%;background:rgba(0,0,0,.18)}
  .relax .icon-placeholder{width:48px;height:48px}
  .relax-note{font-size:12px;color:#e6f7fb;margin-top:4px}
  .item{display:flex;align-items:center;padding:0 10px 0 8px;font-size:14.5px;line-height:1.05;color:var(--navy)}
  .item::before{content:"✓";margin-right:5px;font-size:14px;align-self:center}
  .item.light{background:var(--cyan-light)}
  .item.plain{background:var(--cyan)}
  .grow .item{color:#fff;padding-left:12px}
  .grow .item.grey{background:var(--grey-row);color:#eef0f2}
  .grow .item.dark{background:var(--black)}

  .extras{position:absolute;left:56px;top:1012px}
  .extras h2,.contact h2{font-size:19px;font-weight:700;line-height:1;margin-bottom:6px}
  .extras li{list-style:none;font-size:14.5px;color:var(--muted);line-height:21px}
  .extras li::before{content:"✓";color:var(--ink);margin-right:8px}
  .extras .wrap{padding-left:20px;margin-top:-2px}
  .contact{position:absolute;right:51px;top:1012px;text-align:right}
  .contact-line{display:flex;justify-content:flex-end;align-items:center;font-size:14.5px;color:var(--muted);line-height:21px}
  .contact-line svg{width:13px;height:13px;margin-left:8px;fill:#666}
  .contact .gap{margin-top:3px}
</style>
</head>
<body>
<main class="flyer">
  <div class="intro-panel"></div>
  <div class="shop-photo" role="img" aria-label="Photo of a cozy retail cafe counter with pastry case and menu boards"></div>
  <div class="accent-band"></div>

  <div class="brand">
    <div class="brand-name">brightway</div>
    <div class="brand-sub">TAX AND ACCOUNTING INC.</div>
  </div>

  <p class="tagline">We know you <em>CAN</em> do<br>The <em>ACCOUNTING,</em> but<br>do you <em>WANT</em> to?</p>
  <h1 class="title"><div class="line1">Accounting</div><div class="line2">Packages</div></h1>
  <p class="price">STARTING AT <b>$300</b>/MO)?</p>

  <section class="package develop">
    <div class="pill">DEVELOP</div>
    <div class="icon-slot"><div class="icon-placeholder" role="img" aria-label="Lightbulb idea illustration"></div></div>
    <div class="item light" style="height:41px;margin-top:8px">LedgerLine Online subscription</div>
    <div class="item plain" style="height:36px">Free accounting setup</div>
    <div class="item light" style="height:41px">Weekly transaction processing</div>
    <div class="item plain" style="height:48px">Monthly account reconciliation (up to 2 accounts)</div>
    <div class="item light" style="height:65px">Monthly financial statements by the 15th of the month</div>
  </section>

  <section class="package grow">
    <div class="pill">GROW</div>
    <div class="icon-slot">
      <svg width="80" height="68" viewBox="0 0 80 68" aria-hidden="true">
        <g fill="#fff">
          <rect x="10" y="38" width="12" height="28"/>
          <rect x="27" y="30" width="12" height="36"/>
          <rect x="44" y="38" width="12" height="28"/>
          <polygon points="8,40 30,18 46,32 64,12 58,8 76,2 72,20 68,15 46,40 30,26 12,44"/>
        </g>
      </svg>
    </div>
    <div class="item grey" style="height:50px">LedgerLine Online subscription</div>
    <div class="item dark" style="height:34px">Free accounting setup</div>
    <div class="item grey" style="height:47px">Weekly transaction processing</div>
    <div class="item dark" style="height:48px">Monthly account reconciliation (up to 4 accounts)</div>
    <div class="item grey" style="height:47px">Monthly financial statements by the 10th of the month</div>
    <div class="item dark" style="height:45px">Client portal access for document sharing</div>
    <div class="item grey" style="height:39px">1 Custom Report</div>
    <div class="item dark" style="height:50px">Accounts Payable</div>
    <div class="item grey" style="height:68px">Monthly Scorecard (customized metric tracking for your business)</div>
  </section>

  <section class="package relax">
    <div class="pill">RELAX</div>
    <div class="icon-slot">
      <div class="icon-placeholder" role="img" aria-label="Illustration of a person relaxing in a chair"></div>
      <div class="relax-note">(We've Got This)</div>
    </div>
    <div class="item light" style="height:42px;margin-top:2px">LedgerLine Online subscription</div>
    <div class="item plain" style="height:26px">Free accounting setup</div>
    <div class="item light" style="height:28px">Weekly transaction processing</div>
    <div class="item plain" style="height:41px">Monthly account reconciliation (up to 5-10 accounts)</div>
    <div class="item light" style="height:41px">Monthly financial statements by the 5th of the month</div>
    <div class="item plain" style="height:42px">Client portal access for document sharing</div>
    <div class="item light" style="height:29px">2 Custom Reports</div>
    <div class="item plain" style="height:25px">Accounts Payable</div>
    <div class="item light" style="height:38px">Invoicing and accounts receivable</div>
    <div class="item plain" style="height:57px">Weekly Scorecard (customized metric tracking for your business)</div>
  </section>

  <section class="extras">
    <h2>ADDITIONAL OPTIONS</h2>
    <ul>
      <li>Payroll – 1-10 employees $85/mo;</li>
      <li class="wrap">11-30 employees $175/mo</li>
      <li>Sales tax - $30/mo per state</li>
      <li>Corporate taxes $50/mo</li>
      <li>Owner taxes - $25/mo</li>
    </ul>
  </section>

  <section class="contact">
    <h2>BRIGHTWAY TAX AND ACCOUNTING INC.</h2>
    <div class="contact-line">4810 W. Elm Street
      <svg viewBox="0 0 24 24"><path d="M12 2a7 7 0 0 0-7 7c0 5 7 13 7 13s7-8 7-13a7 7 0 0 0-7-7zm0 9.5A2.5 2.5 0 1 1 12 6.5a2.5 2.5 0 0 1 0 5z"/></svg></div>
    <div class="contact-line" style="margin-right:21px">Riverton, KS 66000</div>
    <div class="contact-line gap">(555) 014-2290
      <svg viewBox="0 0 24 24"><path d="M6.6 10.8a15 15 0 0 0 6.6 6.6l2.2-2.2a1 1 0 0 1 1-.25 11.4 11.4 0 0 0 3.6.57 1 1 0 0 1 1 1V20a1 1 0 0 1-1 1A17 17 0 0 1 3 4a1 1 0 0 1 1-1h3.5a1 1 0 0 1 1 1c0 1.25.2 2.45.57 3.6a1 1 0 0 1-.25 1z"/></svg></div>
    <div class="contact-line gap">accounting@brightway-books.com
      <svg viewBox="0 0 24 24"><path d="M2 5h20v14H2z"/></svg></div>
    <div class="contact-line gap">www.brightwaybooks.com
      <svg viewBox="0 0 24 24"><path d="M12 2a10 10 0 1 0 0 20 10 10 0 0 0 0-20zm-1 2.1V8H7.3A8 8 0 0 1 11 4.1zm2 0A8 8 0 0 1 16.7 8H13zM4.6 10H11v4H4.6a8 8 0 0 1 0-4zm8.4 0h6.4a8 8 0 0 1 0 4H13zm-5.7 6H11v3.9A8 8 0 0 1 7.3 16zm5.7 0h3.7A8 8 0 0 1 13 19.9z"/></svg></div>
  </section>

  <div class="footer-band"></div>
</main>
</body>
</html>
```